Kirenu Tavern Sushi & Sake House

We need business card size flyer that will show our restaurant Logo (attached) with some sushi pictures and our address and phone number.
The flyer is specifically for 10% OFF all Alchohol beverage. Its a japanese sushi house so if you have some extra ideas to spice up the look, please advise.
Also the Address is:
418 W Marlowe Blvd
Pasadena CA 91342

Phone number: 626-555-0193

```html
<!DOCTYPE html>
<html lang="en">
<head>
<meta charset="utf-8">
<title>Kirenu Tavern Sushi &amp; Sake House — 10% Off Flyer</title>
<link href="https://fonts.googleapis.com/css2?family=Oswald:wght@500;700&family=Permanent+Marker&display=swap" rel="stylesheet">
<style>
  :root {
    --page-bg: #e9e6e1;
    --card-dark: #120d0b;
    --bar-brown: #2e1d14;
    --bar-amber: #5a3a22;
    --wood-tray: #4a2a1a;
    --sake-gold: #b48a3e;
    --sake-green: #2f4a22;
    --accent-red: #d9262b;
    --band-red: #d3191f;
    --text-white: #ffffff;
    --sushi-salmon: #e8744a;
    --sushi-rice: #f1ebe1;
    --sushi-nori: #1d1d1b;
  }
  * { box-sizing: border-box; margin: 0; padding: 0; }
  html, body { width: 1200px; height: 1000px; overflow: hidden; }
  body {
    background: var(--page-bg);
    display: flex;
    align-items: center;
    justify-content: center;
    font-family: "Oswald", "Arial Narrow", sans-serif;
  }
  .flyer {
    position: relative;
    width: 1000px;
    height: 590px;
    background: linear-gradient(90deg, var(--card-dark) 0%, #1c130f 50%, var(--bar-brown) 100%);
    overflow: hidden;
    box-shadow: 0 10px 30px rgba(0,0,0,.25);
  }
  .sake-photo {
    position: absolute;
    left: 560px;
    top: 30px;
    width: 410px;
    height: 270px;
    border-radius: 6px;
    background: linear-gradient(160deg, var(--bar-amber) 0%, var(--sake-gold) 35%, var(--sake-green) 65%, var(--wood-tray) 100%);
  }
  .sushi-photo {
    position: absolute;
    left: 620px;
    top: 325px;
    width: 210px;
    height: 150px;
    border-radius: 6px;
    background: linear-gradient(135deg, var(--sushi-salmon) 0%, var(--sushi-rice) 50%, var(--sushi-nori) 100%);
  }
  .headline {
    position: absolute;
    left: 60px;
    top: 150px;
    line-height: 1;
  }
  .headline-discount {
    font-family: "Permanent Marker", "Comic Sans MS", cursive;
    font-weight: 400;
    color: var(--accent-red);
    font-size: 90px;
    display: block;
    margin-bottom: -4px;
  }
  .headline-line {
    display: block;
    color: var(--text-white);
    font-weight: 700;
    text-transform: uppercase;
    letter-spacing: -1px;
  }
  .headline-line.small { font-size: 66px; }
  .headline-line.large { font-size: 104px; margin-top: -6px; }
  .headline-rule {
    width: 330px;
    height: 6px;
    background: var(--accent-red);
    margin-top: 8px;
  }
  .brand {
    position: absolute;
    left: 60px;
    top: 440px;
    display: flex;
    align-items: center;
    gap: 12px;
    color: var(--text-white);
    font-size: 26px;
    font-weight: 500;
  }
  .brand-dot {
    width: 36px;
    height: 36px;
    border-radius: 50%;
    background: var(--accent-red);
  }
  .contact-band {
    position: absolute;
    left: 0; right: 0; bottom: 0;
    height: 72px;
    background: var(--band-red);
    display: flex;
    align-items: center;
    justify-content: space-between;
    padding: 0 40px;
    color: var(--text-white);
    font-weight: 500;
    font-size: 22px;
    letter-spacing: .5px;
    text-transform: uppercase;
  }
</style>
</head>
<body>
  <section class="flyer">
    <div class="sake-photo" role="img" aria-label="Photo of three sake bottles with filled glasses on a wooden bar tray"></div>
    <div class="sushi-photo" role="img" aria-label="Photo of salmon and avocado sushi rolls"></div>

    <h1 class="headline">
      <span class="headline-discount">10% Off</span>
      <span class="headline-line small">All Alcohol</span>
      <span class="headline-line large">Beverage</span>
      <span class="headline-rule" style="display:block"></span>
    </h1>

    <div class="brand">
      <span class="brand-dot"></span>
      <span class="brand-name">Kirenu Tavern</span>
    </div>

    <footer class="contact-band">
      <span class="contact-web">www.kirenutavernpasadena.com</span>
      <span class="contact-address">418 W Marlowe Blvd &nbsp; Pasadena CA 91342</span>
      <span class="contact-phone">626-555-0193</span>
    </footer>
  </section>
</body>
</html>
```